Website for Dental Office - The Brightcrest Clinic

The brightcrest clinic is a dental office offering cosmetic dentistry, general dentistry, and multi-specialty dental care all under one roof in our state-of-the-art cosmetic dental center. We are particularly striving to provide services that fit the need of the young generation. Thus, we hope to have a modern, professional concise website that represents our spirit.

*Should be able to switch from English to Chinese

6 sections besides homepage:
Home, Meet us, Services,
Patient Info, Cases&Reviews, Blog, Contact

The Services sections should contain multiple subsections such as cleaning and prevention, cosmetic dentistry, implant dentistry, removable dentures, etc...
The Patient Info section is also intended to contain several subsections such as
New Patient offer, accepted Insurance, patient portal, helpful tips, etc...

Target Market(s)

young generation

Coding

Number of Pages Required

5+ page

Font styles to use
Sans Serif

Colors
0592cd
33a6d7
85cae6
00a990
33b8a4
86cfc6
cee9f5
cfeae6
3277b5

Requirements
Must have
• *Should be able to switch from English to Chinese
Nice to have
• http://www.thebrightcrestclinic-example.com/
• As a reference, the above link is the current website, but we would like to change the appearance and the content (our new logo's picture is attached)

```html
<!DOCTYPE html>
<html lang="en">
<head>
<meta charset="utf-8">
<title>The Brightcrest Clinic</title>
<link href="https://fonts.googleapis.com/css2?family=Poppins:wght@400;500;600;700&display=swap" rel="stylesheet">
<style>
:root{
  --blue:#0592cd;
  --blue-mid:#33a6d7;
  --blue-soft:#85cae6;
  --blue-pale:#cee9f5;
  --blue-card:#6fbbdf;
  --blue-deep:#3277b5;
  --ink:#222;
  --text:#555;
  --band:#e8f6fc;
  --footer:#1f2326;
}
*{margin:0;padding:0;box-sizing:border-box}
html,body{width:1200px;height:4006px;overflow:hidden}
body{font-family:'Poppins',sans-serif;color:var(--ink);background:#fff;position:relative}
.abs{position:absolute}
.photo{position:absolute}
/* header */
.brand{left:112px;top:20px;display:flex;align-items:center;gap:14px}
.brand-mark{width:52px;height:52px;background:var(--blue-mid);border-radius:8px}
.brand-name{font-weight:600;font-size:26px;line-height:27px;color:var(--blue-mid);text-transform:uppercase}
.contact-pill{display:flex;align-items:center;gap:14px;top:22px}
.contact-icon{width:54px;height:54px;border-radius:10px;background:var(--blue-mid);display:flex;align-items:center;justify-content:center}
.contact-pill small{display:block;font-size:13px;font-weight:600}
.contact-pill strong{font-size:22px;font-weight:600}
.nav{top:94px;left:112px;display:flex;height:37px;align-items:center}
.nav a{font-size:13px;font-weight:500;color:var(--ink);text-decoration:none;text-transform:uppercase;padding:0 25px;height:37px;line-height:37px}
.nav a.active{background:var(--blue-soft);color:#fff;padding:0 19px}
.lang{top:100px;left:990px;display:flex;align-items:center;gap:6px;font-size:14px;font-weight:600}
.flag{width:36px;height:20px;background:linear-gradient(#b22 0 50%,#fff 50% 60%,#b22 60% 100%);position:relative}
.flag::before{content:"";position:absolute;left:0;top:0;width:16px;height:11px;background:#2a3d8f}
/* hero */
.hero{left:0;top:131px;width:1200px;height:680px}
.hero-title{left:112px;top:278px;font-size:54px;line-height:60px}
.hero-title b{color:var(--blue);font-weight:700;display:block}
.hero-title span{font-weight:400;color:var(--ink);display:block}
.btn{display:inline-block;background:var(--blue);color:#fff;font-weight:600;font-size:15px;text-transform:uppercase;border-radius:6px;text-align:center}
/* sections */
.h2{font-size:38px;font-weight:600;text-align:center;text-transform:uppercase;color:var(--ink)}
.center{left:0;width:1200px;text-align:center}
.services{left:0;top:1260px;width:1200px;height:452px;background:linear-gradient(90deg,#e4f1f7,#d6ebf3 50%,#eef6fa)}
.svc{position:absolute;top:160px;width:200px;text-align:center}
.svc .ring{width:142px;height:142px;border-radius:50%;background:var(--blue-mid);margin:0 auto 14px;display:flex;align-items:center;justify-content:center;box-shadow:0 0 0 4px #fff8}
.svc p{font-size:18px;font-weight:500;line-height:28px;text-transform:uppercase}
.arrow{top:1476px;width:32px;height:32px}
.pcard{left:624px;top:1810px;width:430px;height:430px;background:var(--blue-card);border-radius:6px;color:#fff;padding:20px 42px 0 92px}
.pcard h3{font-size:38px;font-weight:600;margin-bottom:10px}
.pcard p{font-size:15px;line-height:28.4px;text-align:justify}
.band{left:0;top:2600px;width:1200px;height:1017px;background:var(--band)}
.offer{position:absolute;top:2475px;width:286px;height:248px;border-radius:4px}
.offer-label{position:absolute;top:2690px;width:242px;height:56px;line-height:56px;background:var(--blue-mid);color:#fff;font-weight:600;font-size:18px;text-align:center;border-radius:4px;text-transform:uppercase}
.doc{position:absolute;left:620px;width:560px;height:175px}
.doc .avatar{position:absolute;left:0;top:0;width:175px;height:175px;border-radius:50%;border:4px solid #fff;box-shadow:0 0 0 1px #ddd}
.doc .info{position:absolute;left:195px;top:22px;font-size:18px;line-height:28px;text-transform:uppercase}
.doc h4{font-weight:600;font-size:18px;margin-bottom:6px}
.doc a{color:var(--blue);font-weight:600;text-decoration:none;font-size:18px;display:inline-block;margin-top:6px;margin-left:3px}
footer{position:absolute;left:0;top:3617px;width:1200px;height:389px;background:var(--footer);color:#fff}
footer h5{position:absolute;top:82px;font-size:18px;font-weight:500;text-transform:uppercase}
.frow{position:absolute;display:flex;gap:16px;font-size:15px;line-height:28px}
.post{position:absolute;left:480px;display:flex;gap:16px;font-size:15px;line-height:28px}
.post .thumb{width:82px;height:82px;background:linear-gradient(135deg,#c98f7d,#4a86b8)}
.post em{font-style:normal;color:#ddd;font-size:15px}
.copy{position:absolute;top:352px;width:1200px;text-align:center;font-size:15px}
</style>
</head>
<body>

<header>
  <div class="abs brand"><div class="brand-mark"></div><div class="brand-name">The Brightcrest<br>Clinic</div></div>
  <div class="abs contact-pill" style="left:568px">
    <div class="contact-icon"><svg width="26" height="26" viewBox="0 0 24 24"><path fill="#fff" d="M6.6 10.8a15 15 0 0 0 6.6 6.6l2.2-2.2c.3-.3.7-.4 1-.2 1.1.4 2.3.6 3.6.6.6 0 1 .4 1 1V20c0 .6-.4 1-1 1A17 17 0 0 1 3 4c0-.6.4-1 1-1h3.5c.6 0 1 .4 1 1 0 1.3.2 2.5.6 3.6.1.3 0 .7-.2 1z"/></svg></div>
    <div><small>CALL US TODAY:</small><strong>1-555-204-7781</strong></div>
  </div>
  <div class="abs contact-pill" style="left:870px">
    <div class="contact-icon"><svg width="24" height="28" viewBox="0 0 24 28"><path fill="#fff" d="M12 1a9 9 0 0 0-9 9c0 7 9 17 9 17s9-10 9-17a9 9 0 0 0-9-9zm0 12a3 3 0 1 1 0-6 3 3 0 0 1 0 6z"/></svg></div>
    <div><small style="line-height:28px">27 HARBOR LANE<br>SUITE 12</small></div>
  </div>
  <nav class="abs nav">
    <a class="active" href="#">Home</a><a href="#">Meet us</a><a href="#">Services</a><a href="#">Patient Info</a><a href="#">Cases&amp;Reviews</a><a href="#">Blog</a><a href="#">Contact</a>
  </nav>
  <div class="abs lang"><span class="flag"></span>ENG <svg width="10" height="6" viewBox="0 0 10 6"><path d="M1 1l4 4 4-4" stroke="#222" fill="none" stroke-width="1.5"/></svg></div>
</header>

<section>
  <svg class="abs hero" viewBox="0 0 1200 680" role="img" aria-label="Photo of a dentist examining a smiling patient's teeth">
    <defs><linearGradient id="heroBg" x1="0" x2="1"><stop offset="0" stop-color="#e9eef2"/><stop offset=".5" stop-color="#d7dde3"/><stop offset="1" stop-color="#b9c3d6"/></linearGradient></defs>
    <path d="M0 0H1200V575Q600 730 0 575Z" fill="url(#heroBg)"/>
    <circle cx="571" cy="566" r="8" fill="#999"/><circle cx="591" cy="567" r="6" fill="#555"/><circle cx="608" cy="567" r="6" fill="#555"/><circle cx="625" cy="567" r="6" fill="#555"/>
    <path d="M215 622Q600 700 980 622" stroke="var(--blue)" stroke-width="7" fill="none"/>
    <circle cx="215" cy="622" r="19" fill="var(--blue)"/><circle cx="980" cy="622" r="19" fill="var(--blue)"/>
  </svg>
  <h1 class="abs hero-title"><b>We Will</b><b>Take Care</b><span>of Your Teeth</span></h1>
  <a class="abs btn" style="left:112px;top:475px;width:152px;height:45px;line-height:45px">Get Started</a>
</section>

<section>
  <h2 class="abs center h2" style="top:895px">Welcome</h2>
  <p class="abs center" style="top:953px;color:var(--blue-soft);font-style:italic;font-weight:500;font-size:18px">“YOUR SMILE. OUR PASSION.”</p>
  <p class="abs" style="left:225px;top:990px;width:750px;text-align:center;font-size:15.5px;line-height:28.4px;color:var(--text)">Welcome to The Brightcrest Clinic where we specialize in General and Cosmetic Dentistry, Dental Implants, Periodontics (Gum Surgery), Endodontics (Root Canal Treatment) and Reconstructive Dentistry for patients in Boston, Brookline, Cambridge, Brighton, Allston, Newton, Watertown, Wellesley and all other surrounding neighborhoods of Boston, Massachusetts.</p>
  <a class="abs btn" style="left:483px;top:1122px;width:234px;height:48px;line-height:48px">Request Appointment</a>
</section>

<section class="abs services">
  <h2 class="h2" style="margin-top:65px">Our Services</h2>
  <div class="svc" style="left:111px"><div class="ring"><svg width="70" height="70" viewBox="0 0 70 70" fill="none" stroke="#fff" stroke-width="3"><path d="M22 22c6-4 10 0 13 0s7-4 13 0c5 4 3 14 0 20-2 6-2 18-6 18-3 0-3-12-7-12s-4 12-7 12c-4 0-4-12-6-18-3-6-5-16 0-20z"/><path d="M12 12l5 5M58 12l-5 5M35 4v7"/></svg></div><p>Cleaning &amp;<br>Prevention</p></div>
  <div class="svc" style="left:370px"><div class="ring"><svg width="70" height="70" viewBox="0 0 70 70" fill="none" stroke="#fff" stroke-width="3"><path d="M14 18c6-4 10 0 13 0s7-4 13 0c5 4 3 14 0 20-2 6-2 18-6 18-3 0-3-12-7-12s-4 12-7 12c-4 0-4-12-6-18-3-6-5-16 0-20z"/><circle cx="50" cy="42" r="10"/><path d="M45 42l4 4 6-7"/></svg></div><p>Cosmetic<br>Dentistry</p></div>
  <div class="svc" style="left:629px"><div class="ring"><svg width="70" height="70" viewBox="0 0 70 70" fill="none" stroke="#fff" stroke-width="3"><path d="M20 12c6-4 10 0 15 0s9-4 15 0c4 3 2 12-2 16H22c-4-4-6-13-2-16z"/><path d="M26 34h18M27 41h16M29 48h12M31 55h8M33 62h4"/></svg></div><p>Implant<br>Dentistry</p></div>
  <div class="svc" style="left:888px"><div class="ring"><svg width="70" height="70" viewBox="0 0 70 70" fill="none" stroke="#fff" stroke-width="3"><path d="M18 14c6-4 11 0 17 0s11-4 17 0c5 4 3 14 0 20-2 6-2 22-6 22-3 0-4-16-11-16s-8 16-11 16c-4 0-4-16-6-22-3-6-5-16 0-20z"/><path d="M24 22c4-2 6 0 9 0"/></svg></div><p>Removable<br>Dentures</p></div>
</section>
<svg class="abs arrow" style="left:38px" viewBox="0 0 32 32"><circle cx="16" cy="16" r="14" fill="none" stroke="#888" stroke-width="3"/><path d="M22 16H10M15 10l-6 6 6 6" stroke="#888" stroke-width="3" fill="none"/></svg>
<svg class="abs arrow" style="left:1130px" viewBox="0 0 32 32"><circle cx="16" cy="16" r="14" fill="none" stroke="#888" stroke-width="3"/><path d="M10 16h12M17 10l6 6-6 6" stroke="#888" stroke-width="3" fill="none"/></svg>

<section>
  <div class="photo" style="left:147px;top:1810px;width:431px;height:430px;border-radius:6px;background:linear-gradient(160deg,#dfe9f0,#8fb8d8 60%,#3a5f9a)" role="img" aria-label="Photo of a smiling young man in a blue shirt"></div>
  <svg class="abs" style="left:490px;top:1990px" width="200" height="40" viewBox="0 0 200 40"><path d="M23 20Q65 40 98 20M134 20Q170 0 195 20" stroke="#fff" stroke-width="6" fill="none"/><path d="M98 20Q116 30 134 20" stroke="#fff" stroke-width="6" fill="none"/><circle cx="23" cy="20" r="18" fill="#fff"/><circle cx="195" cy="20" r="18" fill="#fff"/></svg>
  <div class="abs pcard">
    <h3>PATIENT INFO</h3>
    <p>Thank you for your trust in us. We look forward to working with you towards a healthy and beautiful smile.<br>Prior to your first appointment, we request that you please download and complete:<br>The New Patient Form – Adults or The New Patient Form – Children (16 &amp; Under).</p>
    <a class="btn" style="background:#fff;color:var(--blue);width:236px;height:48px;line-height:48px;margin-top:18px;font-size:14px">View More Info</a>
  </div>
</section>

<div class="abs band"></div>
<section>
  <h2 class="abs center h2" style="top:2362px">We Offer</h2>
  <p class="abs center" style="top:2418px;color:var(--blue-soft);font-weight:600;font-size:18px">PATIENT CARE</p>
  <div class="offer" style="left:112px;background:linear-gradient(135deg,#8ea6c6,#e8ddd6 60%,#4a8ad0)" role="img" aria-label="Close-up photo of a dental mirror near white teeth"></div>
  <div class="offer" style="left:445px;background:linear-gradient(135deg,#e8c9b8,#b06d64 55%,#9fb3e0)" role="img" aria-label="Photo of a dentist examining a patient's open mouth"></div>
  <div class="offer" style="left:778px;background:linear-gradient(135deg,#d9e4ea,#e6d3c2 55%,#c79a82)" role="img" aria-label="Photo of a technician shaping a dental prosthesis"></div>
  <div class="offer-label" style="left:178px">Cosmetic Dentistry</div>
  <div class="offer-label" style="left:511px">General Dentistry</div>
  <div class="offer-label" style="left:845px">Multi-Specialty</div>
</section>

<section>
  <div class="photo" style="left:30px;top:2860px;width:530px;height:750px;background:linear-gradient(180deg,#e8eef4,#ffffff 45%,#dfe7ef);border-radius:240px 240px 0 0" role="img" aria-label="Photo of a smiling female dentist in a white coat pointing to the side"></div>
  <h2 class="abs h2" style="left:620px;top:2896px;text-align:left">Meet Our Doctors</h2>
  <div class="doc" style="top:2975px"><div class="avatar" style="background:linear-gradient(160deg,#d9c9b6,#3b2c28)" role="img" aria-label="Portrait photo of the orthodontist"></div><div class="info"><h4>Lena Morrow, DMD, MS</h4>Board Certified<br>Orthodontist<br><a href="#">View Details ⊙</a></div></div>
  <div class="doc" style="top:3163px"><div class="avatar" style="background:linear-gradient(160deg,#e8e8e8,#1e1e1e)" role="img" aria-label="Portrait photo of the pediatric dentist"></div><div class="info"><h4>Peter J. Holloway, DMD</h4>Board Certified<br>Pediatric Dentist<br><a href="#">View Details ⊙</a></div></div>
  <div class="doc" style="top:3352px"><div class="avatar" style="background:linear-gradient(160deg,#e4dcd2,#6b4a3a)" role="img" aria-label="Portrait photo of the general dentist"></div><div class="info"><h4>Dr. Nadia Farrell, DMD</h4>General<br>Dentist<br><a href="#">View Details ⊙</a></div></div>
</section>

<footer>
  <h5 style="left:110px">Contact Us</h5>
  <div class="frow" style="left:110px;top:122px"><svg width="26" height="32" viewBox="0 0 24 30" fill="none" stroke="var(--blue-mid)" stroke-width="1.6"><path d="M12 2a9 9 0 0 0-9 9c0 7 9 17 9 17s9-10 9-17a9 9 0 0 0-9-9z"/><circle cx="12" cy="11" r="3"/></svg><span style="margin-left:4px">27 Harbor Lane<br>Suite 12</span></div>
  <div class="frow" style="left:110px;top:200px"><svg width="30" height="30" viewBox="0 0 24 24" fill="none" stroke="var(--blue-mid)" stroke-width="1.4"><path d="M6.6 10.8a15 15 0 0 0 6.6 6.6l2.2-2.2 4.6 1.4V20c0 .6-.4 1-1 1A17 17 0 0 1 3 4c0-.6.4-1 1-1h3.5l1.4 4.6z"/></svg><span>1-555-204-7781</span></div>
  <div class="frow" style="left:110px;top:250px"><svg width="30" height="30" viewBox="0 0 24 24" fill="none" stroke="var(--blue-mid)" stroke-width="1.4"><rect x="3" y="6" width="18" height="13"/><path d="M3 6l9 7 9-7"/></svg><span>info@brightcrestclinic-example.com</span></div>
  <h5 style="left:480px">Latest Blog</h5>
  <div class="post" style="top:122px"><div class="thumb" role="img" aria-label="Blog thumbnail photo of a dental visit"></div><div>Sed ut perspiciatis<br>unde omnis iste natus<br><em><span style="color:var(--blue-mid)">▦</span> May 5, 2019</em></div></div>
  <div class="post" style="top:220px"><div class="thumb" role="img" aria-label="Blog thumbnail photo of a smiling patient"></div><div>Sed ut perspiciatis<br>unde omnis iste natus<br><em><span style="color:var(--blue-mid)">▦</span> May 5, 2019</em></div></div>
  <h5 style="left:838px">Newsletter</h5>
  <div class="abs" style="left:838px;top:121px;width:251px;height:42px;background:#fff;color:#666;font-size:14px;line-height:42px;padding-left:16px">Email Address</div>
  <a class="abs btn" style="left:838px;top:172px;width:94px;height:42px;line-height:42px;font-size:14px">Submit</a>
  <p class="copy">© 2019 The Brightcrest Clinic | All Rights Reserved</p>
</footer>

</body>
</html>
```